依頼詳細
潜在意識を開花させる日本生まれの新数秘術を世の中に広めるための認知活動として、1000人無料鑑定キャンペーンを実施予定。
それに使用するランディングページのヘッダーを作成していただきたい。
人生が好転していくキラキラした光が溢れるイメージ。対象は、女性。

色のイメージは、黄色、金、オレンジ、光
記載項目
お金もチャンスもわしづかみ
数字と魂の色で
幸運体質になる黄金法則を初公開!
先着1000名様に無料鑑定プレゼント

特に、4行目のところを目立たせてほしいです。
サイズ
• 横1300✖️縦957 単位は、ピクセル
希望イメージ
シンプル 複雑
単色 カラフル
暗い 明るい
日常 高級
遊び心 厳粛
未来的 伝統的
女性的 男性的
希望する色
黄・オレンジ系、金
納品ファイル
• 高解像度JPG (.jpg)
• イラストレーター形式 (.ai)
• フォトショップ形式 (.psd)
• PNG形式 (.png)
補足説明
当LPを閲覧する人の80%程度は、スマホでの閲覧と想定されます。
スマホで閲覧してもPCからの閲覧でも、どちらでも綺麗に表示できるようにお願いいたします。
サイズは、横1300✖️縦957でお願いします。

キラキラしたイメージであればゴールドにこだわりません。
キャッチコピーを下記に変更ください。
誕生数秘✖️量子力学✖️潜在意識
幸運を呼び込む奇跡のメソッド
秘められた潜在能力点火法を大公開
下記の人物画像と素材人物の2パターンお願いします。

イメージLPを参考にして下さい
先着1000人無料鑑定プレゼントも入れて下さい。
■ 選んだ理由

全体の構成や、文字や色の漢字など、イメージ通りのデザインでした。

■ 提案者全員のお礼・コメント

はじめての試みでしたが、たくさんのデザインをご提案いただきありがとうございました。
今後ともよろしくお願いいたします。

```html
<!DOCTYPE html>
<html lang="ja">
<head>
<meta charset="utf-8">
<title>潜在能力点火法 無料鑑定キャンペーン</title>
<link href="https://fonts.googleapis.com/css2?family=Shippori+Mincho+B1:wght@600;800&display=swap" rel="stylesheet">
<style>
  :root {
    --cream: #fff6e4;
    --gold-light: #fde7a8;
    --gold: #e9bb55;
    --gold-deep: #c9932c;
    --brown: #3d2614;
    --orange: #f0651e;
    --red-orange: #e2401b;
    --white: #ffffff;
  }
  html, body { margin: 0; padding: 0; overflow: hidden; }
  body { width: 1200px; height: 883px; font-family: "Shippori Mincho B1", serif; }
  .header {
    position: relative; width: 1200px; height: 883px; overflow: hidden;
    background:
      radial-gradient(circle at 180px 140px, rgba(255,255,255,.8) 0 30px, transparent 80px),
      radial-gradient(circle at 820px 70px, rgba(255,255,255,.7) 0 20px, transparent 70px),
      radial-gradient(circle at 1080px 200px, rgba(255,255,255,.6) 0 25px, transparent 90px),
      radial-gradient(circle at 80px 520px, rgba(255,255,255,.6) 0 18px, transparent 70px),
      radial-gradient(ellipse at 45% 45%, #fffaf0 0%, var(--cream) 45%, var(--gold-light) 100%);
  }
  .brand { position: absolute; left: 14px; top: 12px; display: flex; flex-direction: column; align-items: center; gap: 6px; }
  .brand-dot { width: 58px; height: 58px; border-radius: 50%; background: var(--gold); }
  .brand-name { font-size: 22px; font-weight: 600; color: var(--gold-deep); }
  .pillar {
    position: absolute; top: 24px; width: 120px; height: 120px; border-radius: 50%;
    border: 2px solid var(--gold); background: rgba(255,255,255,.55);
    display: flex; align-items: center; justify-content: center; text-align: center;
    font-size: 38px; font-weight: 800; line-height: 1.12; color: var(--brown);
  }
  .times { position: absolute; top: 64px; font-size: 30px; color: var(--brown); transform: translateX(-50%); }
  .tagline {
    position: absolute; left: 60px; top: 186px; width: 740px; margin: 0; text-align: center;
    font-size: 36px; font-weight: 800; color: var(--brown); font-style: italic; letter-spacing: 1px;
  }
  .headline { position: absolute; left: 0; width: 860px; text-align: center; font-weight: 800; line-height: 1;
    background: linear-gradient(180deg, var(--orange), var(--red-orange));
    -webkit-background-clip: text; background-clip: text; color: transparent;
    filter: drop-shadow(0 0 3px var(--white)) drop-shadow(0 0 3px var(--white));
  }
  .headline-1 { top: 282px; font-size: 84px; }
  .headline-2 { top: 392px; font-size: 100px; letter-spacing: -2px; }
  .headline-3 { top: 496px; font-size: 116px; left: -37px; }
  .swoosh { position: absolute; left: 130px; top: 614px; }
  .portrait {
    position: absolute; left: 720px; top: 110px; width: 480px; height: 730px;
    background: radial-gradient(ellipse at 55% 35%, #f3d6bf 0%, #fbeee2 45%, rgba(255,246,228,0) 75%);
  }
  .band { position: absolute; left: 0; top: 690px; }
  .badge {
    position: absolute; left: 84px; top: 678px; width: 228px; height: 228px; border-radius: 50%;
    background: var(--white); border: 3px solid var(--gold-light);
    display: flex; flex-direction: column; align-items: center; padding-top: 24px; box-sizing: border-box;
    color: var(--brown); font-weight: 800;
  }
  .badge-lead { font-size: 50px; line-height: 1.1; }
  .badge-count { font-size: 64px; line-height: 1.1; white-space: nowrap; }
  .badge-count small { font-size: 24px; writing-mode: vertical-rl; vertical-align: middle; line-height: 1; }
  .offer { position: absolute; left: 412px; top: 766px; font-size: 79px; font-weight: 800; color: var(--brown); letter-spacing: 1px; white-space: nowrap; }
</style>
</head>
<body>
<div class="header">
  <div class="brand"><span class="brand-dot"></span><span class="brand-name">ルミナの灯</span></div>

  <div class="pillar" style="left:258px">誕生<br>数秘</div>
  <span class="times" style="left:408px">×</span>
  <div class="pillar" style="left:434px">量子<br>力学</div>
  <span class="times" style="left:600px">×</span>
  <div class="pillar" style="left:640px">潜在<br>意識</div>

  <p class="tagline">＼幸運を呼び込む奇跡のメソッド／</p>

  <div class="portrait" role="img" aria-label="白い花柄のワンピースを着て微笑む女性講師の写真"></div>

  <div class="headline headline-1">秘められた</div>
  <div class="headline headline-2">潜在能力点火法を</div>
  <div class="headline headline-3">大公開</div>
  <svg class="swoosh" width="480" height="50" viewBox="0 0 480 50" aria-hidden="true">
    <path d="M0 8 Q200 58 476 10" fill="none" stroke="#e2401b" stroke-width="4" stroke-linecap="round"/>
  </svg>

  <svg class="band" width="1200" height="193" viewBox="0 0 1200 193" aria-hidden="true">
    <defs>
      <linearGradient id="bandGold" x1="0" y1="0" x2="0" y2="1">
        <stop offset="0" stop-color="#fbe39a"/>
        <stop offset="1" stop-color="#e9bb55"/>
      </linearGradient>
    </defs>
    <path d="M0 40 Q600 -10 1200 30 L1200 193 L0 193 Z" fill="url(#bandGold)"/>
    <path d="M0 40 Q600 -10 1200 30" fill="none" stroke="#fff6d8" stroke-width="3"/>
  </svg>

  <div class="badge">
    <span class="badge-lead">先着</span>
    <span class="badge-count">1,000<small>名様</small></span>
  </div>
  <div class="offer">無料鑑定プレゼント</div>
</div>
</body>
</html>
```